Cover for novel by Dorian T. Velkam

I need a book cover for a young adult novel about a group of teenagers fleeing the repressive government of their home country pursued by cruel government agents. They must cross a river to reach a neighboring country where they will be safe. My idea is for a minimalist design, perhaps with a birds-eye view of a rowboat sitting in blue water with the oars crossed. The boat could be an abstract charcoal or pen-and-ink sketch. Of course, I'm open to ideas. Will need the front, spine, and back cover for hardback and paperback editions. Plus, the cover for eBook and audiobook versions. The book's title is: VELVET QUARRY, the author name is Dorian T. Velkam.

```html
<!DOCTYPE html>
<html lang="en">
<head>
<meta charset="utf-8">
<title>Velvet Quarry – Full Cover Wrap</title>
<link rel="stylesheet" href="https://fonts.googleapis.com/css2?family=Anton&family=Crimson+Pro:wght@700&family=Source+Serif+4:opsz,wght@8..60,400&display=swap">
<style>
  :root {
    --navy-deep: #14306a;
    --navy: #1f4488;
    --navy-light: #2e5aa0;
    --water: #5b8cc9;
    --water-mid: #3f6fb3;
    --hull-light: #d4d6da;
    --hull-mid: #b9bfc8;
    --spine-black: #050505;
    --spine-blue: #3d8fd8;
    --paper: #ffffff;
  }
  * { margin: 0; padding: 0; box-sizing: border-box; }
  html, body { width: 1200px; height: 831px; overflow: hidden; background: #ffffff; }
  .cover-wrap { position: relative; width: 1200px; height: 831px; overflow: hidden; }

  .back-cover {
    position: absolute; left: 0; top: 0; width: 551px; height: 831px;
    background:
      radial-gradient(ellipse 300px 220px at 180px 330px, rgba(70,110,180,0.35), transparent 70%),
      radial-gradient(ellipse 260px 200px at 420px 640px, rgba(60,100,170,0.3), transparent 70%),
      radial-gradient(ellipse 340px 240px at 120px 760px, rgba(15,35,80,0.45), transparent 70%),
      linear-gradient(170deg, var(--navy-deep) 0%, var(--navy) 45%, var(--navy-light) 80%, var(--navy) 100%);
  }
  .back-blurb {
    position: absolute; left: 67px; top: 68px; width: 418px;
    font-family: "Source Serif 4", Georgia, serif;
    font-size: 15.6px; line-height: 23.1px;
    color: var(--paper); text-align: justify;
  }
  .back-blurb p + p { margin-top: 23px; }

  .spine {
    position: absolute; left: 551px; top: 0; width: 94px; height: 831px;
    background: var(--spine-black);
  }
  .spine-title {
    position: absolute; left: 47px; top: 319px;
    transform: translate(-50%, -50%) rotate(-90deg);
    font-family: "Anton", Impact, sans-serif;
    font-size: 52px; line-height: 1; color: var(--spine-blue);
    white-space: nowrap; letter-spacing: 0.5px;
  }
  .spine-author {
    position: absolute; left: 48px; top: 608px;
    transform: translate(-50%, -50%) rotate(-90deg);
    font-family: "Crimson Pro", Georgia, serif; font-weight: 700;
    font-size: 30px; line-height: 1; color: var(--paper); white-space: nowrap;
  }

  .front-cover {
    position: absolute; left: 645px; top: 0; width: 555px; height: 831px;
    background:
      radial-gradient(ellipse 200px 150px at 130px 380px, rgba(190,215,240,0.45), transparent 70%),
      radial-gradient(ellipse 220px 160px at 440px 420px, rgba(170,200,235,0.4), transparent 70%),
      radial-gradient(ellipse 240px 180px at 80px 700px, rgba(40,80,150,0.55), transparent 70%),
      radial-gradient(ellipse 300px 160px at 300px 50px, rgba(30,70,140,0.55), transparent 70%),
      radial-gradient(ellipse 220px 170px at 500px 760px, rgba(60,100,170,0.5), transparent 70%),
      linear-gradient(180deg, var(--water-mid) 0%, var(--water) 50%, var(--water-mid) 100%);
  }
  .front-author {
    position: absolute; left: 139px; top: 86px;
    font-family: "Crimson Pro", Georgia, serif; font-weight: 700;
    font-size: 37px; line-height: 1; color: var(--paper); white-space: nowrap;
  }
  .title-band { position: absolute; left: 0; top: 160px; width: 555px; height: 90px; }
  .title-band text { font-family: "Anton", Impact, sans-serif; fill: var(--paper); }

  .boat-illustration {
    position: absolute; left: 118px; top: 345px; width: 300px; height: 311px;
    border-radius: 6px;
    background: linear-gradient(180deg, var(--hull-light) 0%, var(--hull-mid) 60%, #a3b3c6 100%);
  }
</style>
</head>
<body>
<div class="cover-wrap">

  <section class="back-cover">
    <div class="back-blurb">
      <p>Lorem ipsum dolor sit amet, consectetur adipiscing elit. Nunc imperdiet erat elit, sed rutrum odio pellentesque sit amet. Quisque facilisis neque ac suscipit ullamcorper. Ut condimentum neque leo, eget dapibus libero suscipit vel. Aenean vel dui erat. Praesent sit amet leo a mi lacinia mattis euismod at erat. Aliquam hendrerit ipsum ac semper dignissim. Sed sollicitudin, tellus vitae tempor elementum, ex nibh ultricies felis, quis sagittis massa lectus ullamcorper magna. Nunc ac mollis orci, nec congue urna.</p>
      <p>Maecenas ut hendrerit lacus, vel varius ex. Fusce pulvinar tincidunt nunc. Donec iaculis mi ac venenatis placerat. Etiam tincidunt purus et pretium euismod. Sed vestibulum, ipsum quis lacinia ullamcorper, libero orci porta urna, varius semper urna libero quis eros. In et vestibulum neque. Duis vel est at neque efficitur commodo ut sit amet justo.</p>
    </div>
  </section>

  <section class="spine">
    <div class="spine-title">VELVET QUARRY</div>
    <div class="spine-author">Dorian T. Velkam</div>
  </section>

  <section class="front-cover">
    <div class="front-author">Dorian T. Velkam</div>
    <svg class="title-band" viewBox="0 0 555 90" width="555" height="90">
      <rect class="title-band-bar" x="0" y="16" width="514" height="50" fill="#050505"/>
      <text x="37" y="79" font-size="82" textLength="477" lengthAdjust="spacingAndGlyphs">VELVET QUARRY</text>
    </svg>
    <div class="boat-illustration" role="img" aria-label="Charcoal sketch of a rowboat seen from above with crossed oars, drifting on blue water"></div>
  </section>

</div>
</body>
</html>
```